Need a simple buisness card for my plumbing business. Would like it to be black background with white text.

Industry/Entity Type

Business

Requirements
Must have
• On the front of the card I need to have,
TKW PLUMBING SERVICES
PLUMBERS, DRAINERS & GASFITTERS
Dorian Lessop
0491576038
Info@tkwplumbingservices.com.au
LIC No 518047k
ABN No 57091836254
On the back I need in point form
Domestic,industrial,commercial, all new installations, renovations, sewer renewals, repairs,
Fully licensed and insured
Nice to have
• A nice simple logo

```html
<!DOCTYPE html>
<html lang="en">
<head>
<meta charset="utf-8">
<title>TKW Plumbing Services – Business Card</title>
<link rel="stylesheet" href="https://fonts.googleapis.com/css2?family=Arimo:wght@400;700&display=swap">
<style>
  :root {
    --page: #ffffff;
    --stage: #58595b;
    --card: #050505;
    --ink: #ffffff;
    --ink-soft: #bdbdbd;
    --strip: #ffffff;
  }
  * { margin: 0; padding: 0; box-sizing: border-box; }
  html, body {
    width: 1200px;
    height: 791px;
    overflow: hidden;
    background: var(--page);
    font-family: "Arimo", Arial, sans-serif;
  }
  .stage {
    position: absolute;
    inset: 0;
    background: var(--stage);
    border-radius: 27px;
  }
  .card {
    position: absolute;
    left: 380px;
    width: 442px;
    background: var(--card);
    border-radius: 6px;
    overflow: hidden;
    color: var(--ink);
  }
  .card--front { top: 136px; height: 265px; }
  .card--back  { top: 421px; height: 285px; }

  .brand { position: absolute; left: 18px; }
  .card--front .brand { top: 14px; }
  .card--back .brand  { top: 12px; left: 16px; }

  .brand__name {
    font-weight: 700;
    font-size: 29px;
    line-height: 1;
    letter-spacing: 0.2px;
    white-space: nowrap;
  }
  .brand__trade {
    margin-top: 6px;
    font-size: 11.5px;
    letter-spacing: 1.4px;
    word-spacing: 3px;
    color: var(--ink-soft);
    white-space: nowrap;
  }

  .contact {
    position: absolute;
    left: 18px;
    top: 136px;
    list-style: none;
    font-size: 15px;
    line-height: 22px;
    letter-spacing: -0.2px;
    white-space: nowrap;
  }

  .services {
    position: absolute;
    left: 0;
    right: 0;
    top: 150px;
    display: grid;
    grid-template-columns: auto auto;
    justify-content: center;
    column-gap: 34px;
    list-style: none;
    font-size: 14.5px;
    line-height: 22px;
    letter-spacing: -0.2px;
  }
  .services__item {
    position: relative;
    padding-left: 13px;
    white-space: nowrap;
  }
  .services__item::before {
    content: "";
    position: absolute;
    left: 0;
    top: 9px;
    width: 5px;
    height: 5px;
    border-radius: 50%;
    background: var(--ink);
  }
  .strip {
    position: absolute;
    left: 0;
    right: 0;
    bottom: 0;
    height: 36px;
    background: var(--strip);
  }
</style>
</head>
<body>
  <div class="stage">
    <section class="card card--front">
      <header class="brand">
        <h1 class="brand__name">TKW PLUMBING SERVICES</h1>
        <p class="brand__trade">PLUMBERS, DRAINERS &amp; GASFITTERS</p>
      </header>
      <ul class="contact">
        <li>Dorian Lessop</li>
        <li>0491576038</li>
        <li>Info@tkwplumbingservices.com.au</li>
        <li>Lic no: 518047k</li>
        <li>ABN no: 57091836254</li>
      </ul>
    </section>

    <section class="card card--back">
      <header class="brand">
        <h2 class="brand__name">TKW PLUMBING SERVICES</h2>
        <p class="brand__trade">PLUMBERS, DRAINERS &amp; GASFITTERS</p>
      </header>
      <ul class="services">
        <li class="services__item">Domestic</li>
        <li class="services__item">Renovations</li>
        <li class="services__item">Industrial</li>
        <li class="services__item">Sewer renewals</li>
        <li class="services__item">Commercial</li>
        <li class="services__item">Repairs</li>
        <li class="services__item">All new installations</li>
        <li class="services__item">Fully licensed and insured</li>
      </ul>
      <div class="strip"></div>
    </section>
  </div>
</body>
</html>
```